Looking for a Micropage Template

My website will be offering our users to have their very own micropage / profile page hosted on our website.

I am looking for someone to design a a web micropage / profile template that matches the color theme of our websites homepage.

1. Follow the colors of our homepage

2. Open the excel sheet and follow the directions to design a micropage / profile page template.

Target Market(s)

Travel Market

Industry/Entity Type

Travel

Number of Pages Required

1 page

Requirements
Must have
• All of the fields specified in the excel sheet
Nice to have
• Follow the color themes and style of the company homepage
• Different color themes is acceptable as long as it looks nice
• Nice HQ photos

```html
<!DOCTYPE html>
<html lang="en">
<head>
<meta charset="utf-8">
<title>Voyalo – Home</title>
<link rel="stylesheet" href="https://fonts.googleapis.com/css2?family=Arimo:wght@400;700&family=PT+Sans:wght@400;700&family=Open+Sans:wght@400;600&display=swap">
<style>
  :root {
    --teal: #3dbcbc;
    --teal-deep: #2ea9a7;
    --teal-light: #45c4c2;
    --yellow: #f5c02e;
    --ink: #1b1b1b;
    --body-text: #2b2b2b;
    --white: #ffffff;
    --slate: #1f2b33;
    --field-border: #4fc3c1;
    --placeholder: #9a9a9a;
  }
  * { box-sizing: border-box; margin: 0; padding: 0; }
  html, body { width: 978px; height: 1200px; overflow: hidden; }
  body {
    position: relative;
    background: var(--white);
    font-family: "Arimo", Arial, sans-serif;
    color: var(--body-text);
  }

  /* Header */
  .site-header { position: absolute; left: 0; top: 0; width: 978px; height: 91px; background: var(--white); }
  .brand {
    position: absolute; left: 44px; top: 30px;
    display: flex; align-items: center; gap: 8px;
    font-family: "PT Sans", sans-serif; font-weight: 700; font-size: 30px;
    color: var(--teal); line-height: 1;
  }
  .brand-dot { width: 14px; height: 14px; border-radius: 50%; background: var(--yellow); }
  .main-nav { position: absolute; left: 286px; top: 24px; width: 692px; height: 48px; }
  .main-nav svg { position: absolute; inset: 0; }
  .main-nav ul { position: absolute; inset: 0; list-style: none; }
  .main-nav li {
    position: absolute; top: 0; height: 48px; line-height: 48px;
    font-size: 17px; color: var(--white);
  }
  .main-nav li.is-active { background: var(--yellow); padding: 0 12px; }

  /* Hero */
  .hero { position: absolute; left: 0; top: 91px; width: 978px; height: 389px; }
  .hero-photo {
    position: absolute; inset: 0;
    background: linear-gradient(180deg, #5aa9dc 0%, #86c5e8 38%, #3fb6c8 55%, #2aa7bf 68%, #bfe3e6 82%, #e9e2d2 100%);
  }
  .hero-caption {
    position: absolute; right: 0; top: 143px; width: 317px; height: 112px;
    background: rgba(27, 37, 45, 0.9);
    padding: 12px 0 0 30px;
    font-family: "PT Sans", sans-serif; font-size: 29px; line-height: 34px; color: var(--white);
    font-weight: 400;
  }

  /* Intro band */
  .intro-band { position: absolute; left: 0; top: 480px; width: 978px; height: 74px; background: var(--teal-deep); }
  .intro-band svg { position: absolute; left: 0; top: 0; }
  .intro-title { position: absolute; left: 12px; top: 14px; color: var(--white); font-size: 22px; line-height: 26px; font-weight: 400; }
  .intro-subtitle { position: absolute; left: 13px; top: 42px; color: var(--white); font-size: 14px; }
  .intro-text { position: absolute; left: 278px; top: 18px; width: 540px; color: var(--white); font-size: 14.5px; line-height: 19px; }
  .see-more {
    position: absolute; left: 832px; top: 18px; width: 108px; height: 40px;
    border-radius: 10px; border: 1px solid #2a2a2a;
    background: linear-gradient(180deg, #6a6a6a 0%, #3c3c3c 100%);
    color: var(--white); font-size: 17px; line-height: 38px; text-align: center;
  }

  /* Feature cards */
  .feature { position: absolute; top: 576px; width: 303px; }
  .feature-frame {
    height: 156px; padding: 6px; background: var(--white);
    border: 1px solid #cfcfcf; border-radius: 3px;
    box-shadow: 0 8px 10px -6px rgba(0,0,0,0.35);
  }
  .feature-photo { width: 100%; height: 100%; }
  .feature-photo.sea { background: linear-gradient(180deg, #3f7fc6 0%, #7cc0e6 40%, #19b4d3 65%, #2c7f4e 100%); }
  .feature-photo.lobby { background: linear-gradient(180deg, #6b5240 0%, #c9a27a 45%, #7a5a44 75%, #3e2f26 100%); }
  .feature-photo.pool { background: linear-gradient(180deg, #1f3a33 0%, #c98b46 45%, #7d5a33 65%, #2fa9c5 100%); }
  .feature-title { margin-top: 22px; font-size: 18.5px; line-height: 22px; color: var(--ink); font-weight: 400; }
  .feature-text {
    margin-top: 4px; font-size: 13.8px; line-height: 21.6px; color: var(--body-text);
    white-space: nowrap; letter-spacing: -0.1px;
  }

  /* Contact */
  .contact { position: absolute; left: 0; top: 869px; width: 978px; height: 289px; }
  .contact-photo {
    position: absolute; inset: 0;
    background: linear-gradient(180deg, #55626b 0%, #6a767c 45%, #7d7f78 70%, #6f6f68 100%);
  }
  .contact-shade { position: absolute; inset: 0; background: rgba(30, 40, 48, 0.45); }
  .contact-title { position: absolute; left: 0; width: 100%; top: 20px; text-align: center; font-size: 20px; color: var(--white); font-weight: 400; }
  .field {
    position: absolute; background: var(--white);
    border: 1px solid var(--field-border);
    font-family: "Open Sans", sans-serif; font-size: 15px; color: var(--placeholder);
    padding: 7px 8px;
  }
  .send {
    position: absolute; left: 479px; top: 239px; width: 73px; height: 30px;
    background: var(--teal); color: var(--white);
    font-family: "Open Sans", sans-serif; font-size: 13px; font-weight: 600;
    line-height: 30px; text-align: center;
  }

  /* Footer */
  .site-footer { position: absolute; left: 0; top: 1158px; width: 978px; height: 42px; background: var(--teal); }
  .copyright { position: absolute; left: 32px; top: 13px; font-size: 13px; color: var(--white); }
  .social { position: absolute; left: 853px; top: 8px; display: flex; gap: 5px; }
  .social span { width: 26px; height: 26px; background: var(--white); border-radius: 2px; }
</style>
</head>
<body>

<header class="site-header">
  <div class="brand"><span>Voyalo.com</span><span class="brand-dot"></span></div>
  <nav class="main-nav">
    <svg width="692" height="48" viewBox="0 0 692 48" aria-hidden="true">
      <polygon points="14,0 692,0 692,48 0,48" fill="var(--teal)"/>
    </svg>
    <ul>
      <li class="is-active" style="left:37px">Home</li>
      <li style="left:129px">About Us</li>
      <li style="left:235px">Resorts</li>
      <li style="left:325px">Reserve</li>
      <li style="left:418px">Browse</li>
      <li style="left:506px">Login</li>
    </ul>
  </nav>
</header>

<section class="hero">
  <div class="hero-photo" role="img" aria-label="Photo of a smiling family on a sunny tropical beach with turquoise sea"></div>
  <h1 class="hero-caption">Escape to Your<br>Dream Destination</h1>
</section>

<section class="intro-band">
  <svg width="264" height="74" viewBox="0 0 264 74" aria-hidden="true">
    <polygon points="0,0 246,0 264,74 0,74" fill="var(--teal-light)"/>
  </svg>
  <h2 class="intro-title">Lorem Ipsum Dolor</h2>
  <p class="intro-subtitle">Dolorest excite folurn ant fulunt</p>
  <p class="intro-text">Nulla lacinia, elit in consectetur congue, nisi metus sagittis ligula, vitae tincidunt Pellentesque habitant morbi tristique senectus et netus et malesuada fames.</p>
  <div class="see-more">See More</div>
</section>

<article class="feature" style="left:12px">
  <div class="feature-frame"><div class="feature-photo sea" role="img" aria-label="Photo of a tropical bay with a sailboat and palm leaves"></div></div>
  <h3 class="feature-title">Urna Mulisit Qyum Matero</h3>
  <p class="feature-text">Lorem ipsum dolor sit amet, consectetuedipscing<br>elit. Aenean commodo ligula eget dolor. Aenean<br>massa. Cum sociis natoque penatibus et magnis</p>
</article>

<article class="feature" style="left:337px">
  <div class="feature-frame"><div class="feature-photo lobby" role="img" aria-label="Photo of a warmly lit hotel lobby"></div></div>
  <h3 class="feature-title">Cheapest Deals Quisit Et Allum</h3>
  <p class="feature-text">Lorem ipsum dolor sit amet, consectetuedipscing<br>elit. Aenean commodo ligula eget dolor. Aenean<br>massa. Cum sociis natoque penatibus et magnis</p>
</article>

<article class="feature" style="left:662px">
  <div class="feature-frame"><div class="feature-photo pool" role="img" aria-label="Photo of a resort restaurant beside a pool at dusk"></div></div>
  <h3 class="feature-title">Book Your Stay Today</h3>
  <p class="feature-text" style="padding-left:3px">Lorem ipsum dolor sit amet, consectetuedipscing<br>elit. Aenean commodo ligula eget dolor. Aenean<br>massa. Cum sociis natoque penatibus et magnis</p>
</article>

<section class="contact">
  <div class="contact-photo" role="img" aria-label="Faded beach photo of a family playing on the sand"></div>
  <div class="contact-shade"></div>
  <h2 class="contact-title">Contact Us</h2>
  <div class="field" style="left:150px; top:75px; width:347px; height:40px">Name</div>
  <div class="field" style="left:150px; top:123px; width:347px; height:40px">Email</div>
  <div class="field" style="left:150px; top:171px; width:347px; height:40px">Phone Number</div>
  <div class="field" style="left:515px; top:75px; width:345px; height:136px">Message</div>
  <div class="send">Send</div>
</section>

<footer class="site-footer">
  <p class="copyright">All Rights Reserved © 2015 Voyalo</p>
  <div class="social" aria-label="Social links"><span></span><span></span><span></span></div>
</footer>

</body>
</html>
```